Holiday PROMO Flyer for Healthy Restaurant

Hi ! We need a holiday style promo flyer for Verandel . Please have a holiday vibe type of design in the background. Include at least 1 of the photos that I provide, and our logo of course. This promo is for a new package that we will be offering until December 31st 2022.

It will have a promo of some type of design that says the following in a creative way:
" HOLIDAY PACKAGE PROMO!"
Buy our holiday package of $500 and receive a $100 gift card!" (THIS SHOULD BE VERY NOTICEABLE AS THIS IS THE ACTUAL PROMO)
Our biggest promo to date.
Offer ends December 31st, 2022.

Take a look at our website to stay consistant with the brand as well.

Industry/Entity Type

Restaurant

Requirements
Must have
• Logo, food photo and gift card photo

```html
<!DOCTYPE html>
<html lang="en">
<head>
<meta charset="utf-8">
<title>Verandel Holiday Package Promo</title>
<link href="https://fonts.googleapis.com/css2?family=Oswald:wght@400;500;600;700&family=Montserrat:wght@700;800&display=swap" rel="stylesheet">
<style>
  :root {
    --navy: #0e2f5e;
    --green: #8cc63f;
    --green-light: #b4dd6a;
    --green-deep: #6fae25;
    --orange: #f6a627;
    --white: #ffffff;
    --paper: #f4f4f4;
    --grey-texture: #dcdcdc;
    --bun: #d19a5c;
    --bun-light: #e2b27a;
    --bun-deep: #c4874a;
  }
  html, body {
    margin: 0;
    padding: 0;
    width: 960px;
    height: 1200px;
    overflow: hidden;
    background: var(--white);
  }
  .flyer {
    position: relative;
    width: 960px;
    height: 1200px;
    overflow: hidden;
    background: var(--paper);
    font-family: "Oswald", sans-serif;
  }
  .backdrop-photo {
    position: absolute;
    inset: 0;
    background:
      radial-gradient(ellipse at 30% 45%, #e9e9e9 0%, rgba(233,233,233,0) 55%),
      radial-gradient(ellipse at 75% 30%, #e2e2e2 0%, rgba(226,226,226,0) 50%),
      linear-gradient(180deg, #f7f7f7 0%, var(--grey-texture) 55%, #ececec 100%);
  }
  .frame {
    position: absolute;
    left: 34px;
    top: 24px;
    right: 34px;
    bottom: 36px;
    border: 2px solid var(--green);
    pointer-events: none;
    z-index: 5;
  }
  .brand {
    position: absolute;
    top: 38px;
    left: 0;
    right: 0;
    text-align: center;
    z-index: 6;
  }
  .brand-name {
    font-family: "Montserrat", sans-serif;
    font-weight: 800;
    font-size: 84px;
    line-height: 1;
    letter-spacing: 2px;
    color: #8f9294;
    text-transform: uppercase;
  }
  .brand-tagline {
    margin-top: 10px;
    font-family: "Montserrat", sans-serif;
    font-weight: 700;
    font-size: 24px;
    letter-spacing: 0.5px;
    color: var(--green);
  }
  .brand-tagline .divider {
    display: inline-block;
    width: 2px;
    height: 26px;
    background: var(--green);
    margin: 0 16px;
    vertical-align: -5px;
  }
  .headline-band {
    position: absolute;
    left: 0;
    right: 0;
    top: 181px;
    height: 105px;
    background: var(--navy);
    display: flex;
    align-items: center;
    justify-content: center;
    z-index: 6;
  }
  .headline {
    margin: 0;
    font-weight: 700;
    font-size: 78px;
    line-height: 1;
    letter-spacing: 0.5px;
    color: var(--green);
  }
  .headline .accent { color: var(--white); font-weight: 500; }
  .offer-badge {
    position: absolute;
    left: 80px;
    top: 300px;
    width: 370px;
    height: 330px;
    z-index: 6;
  }
  .offer-badge svg { position: absolute; inset: 0; }
  .offer-text {
    position: absolute;
    left: 0;
    right: 0;
    top: 108px;
    margin: 0;
    text-align: center;
    font-weight: 400;
    font-size: 36px;
    line-height: 1.08;
    color: var(--navy);
  }
  .offer-text strong { font-weight: 700; }
  .gift-card {
    position: absolute;
    left: 480px;
    top: 340px;
    width: 400px;
    height: 230px;
    background: var(--navy);
    border-radius: 16px;
    transform: rotate(-8deg);
    box-shadow: 6px 10px 18px rgba(0,0,0,0.35);
    overflow: hidden;
    z-index: 6;
  }
  .gift-card .ribbon-h {
    position: absolute;
    left: 0; right: 0; top: 34px;
    height: 14px;
    background: var(--green);
  }
  .gift-card .ribbon-v {
    position: absolute;
    top: 0; bottom: 0; left: 84px;
    width: 14px;
    background: var(--green);
  }
  .gift-card .card-label {
    position: absolute;
    left: 22px;
    top: 86px;
    writing-mode: vertical-rl;
    font-family: "Montserrat", sans-serif;
    font-weight: 700;
    font-size: 17px;
    letter-spacing: 3px;
    color: var(--green);
  }
  .gift-card .card-name {
    position: absolute;
    left: 122px;
    top: 96px;
    font-family: "Montserrat", sans-serif;
    font-weight: 800;
    font-size: 42px;
    letter-spacing: 1px;
    color: var(--white);
    text-transform: uppercase;
  }
  .gift-card .card-tagline {
    position: absolute;
    left: 124px;
    top: 148px;
    font-family: "Montserrat", sans-serif;
    font-weight: 700;
    font-size: 13px;
    color: var(--green);
    white-space: nowrap;
  }
  .food-photo {
    position: absolute;
    left: 36px;
    top: 618px;
    width: 888px;
    height: 544px;
    border-radius: 18px 18px 0 0;
    background: linear-gradient(180deg, var(--bun-light) 0%, var(--bun) 45%, var(--bun-deep) 100%);
    z-index: 4;
  }
  .closing-tag {
    position: absolute;
    left: 394px;
    right: 0;
    top: 978px;
    height: 124px;
    background: var(--navy);
    border-radius: 26px 0 0 26px;
    box-shadow: 0 6px 14px rgba(0,0,0,0.3);
    display: flex;
    flex-direction: column;
    justify-content: center;
    align-items: flex-end;
    padding-right: 44px;
    z-index: 7;
  }
  .closing-tag p {
    margin: 0;
    font-weight: 400;
    font-size: 38px;
    line-height: 1.15;
    color: var(--white);
  }
  .closing-tag .ends { color: var(--orange); }
  .closing-tag .date { color: var(--green); }
</style>
</head>
<body>
  <main class="flyer">
    <div class="backdrop-photo" role="img" aria-label="Faint greyscale photo of a fresh salad filling the background"></div>
    <div class="frame"></div>

    <header class="brand">
      <div class="brand-name">Verandel</div>
      <div class="brand-tagline">HEALTHY KITCHEN<span class="divider"></span>MEAL PREP</div>
    </header>

    <section class="headline-band">
      <h1 class="headline">HOLIDAY PACKAGE <span class="accent">PROMO!</span></h1>
    </section>

    <section class="offer-badge">
      <svg viewBox="0 0 370 330" width="370" height="330" aria-hidden="true">
        <defs>
          <radialGradient id="badgeFill" cx="50%" cy="30%" r="70%">
            <stop offset="0%" stop-color="#c6e784"/>
            <stop offset="55%" stop-color="#8cc63f"/>
            <stop offset="100%" stop-color="#78b52c"/>
          </radialGradient>
        </defs>
        <polygon fill="url(#badgeFill)" points="
          185,5 199,24 215,7 225,28 244,13 250,36 271,25 273,49 296,42 293,66 317,64 309,87 332,90 320,111 342,119 326,137 345,150 325,165 345,180 326,193 342,211 320,219 332,240 309,243 317,266 293,264 296,288 273,281 271,305 250,294 244,317 225,302 215,323 199,306 185,325 171,306 155,323 145,302 126,317 120,294 99,305 97,281 74,288 77,264 53,266 61,243 38,240 50,219 28,211 44,193 25,180 45,165 25,150 44,137 28,119 50,111 38,90 61,87 53,64 77,66 74,42 97,49 99,25 120,36 126,13 145,28 155,7 171,24"/>
      </svg>
      <p class="offer-text">BUY OUR HOLIDAY<br>PACKAGE OF <strong>$500</strong> &amp;<br>RECEIVE A <strong>$100</strong><br>GIFT CARD!</p>
    </section>

    <aside class="gift-card" aria-label="Verandel gift card">
      <div class="ribbon-h"></div>
      <div class="ribbon-v"></div>
      <span class="card-label">GIFT CARD</span>
      <span class="card-name">Verandel</span>
      <span class="card-tagline">HEALTHY KITCHEN | MEAL PREP</span>
    </aside>

    <div class="food-photo" role="img" aria-label="Photo of a grilled chicken sandwich on a sesame bun with lettuce, tomato and cheese"></div>

    <section class="closing-tag">
      <p>OUR BIGGEST PROMO TO DATE.</p>
      <p><span class="ends">OFFER ENDS</span> <span class="date">DECEMBER 31ST, 2022</span></p>
    </section>
  </main>
</body>
</html>
```